Ready to be wowed! Snazzy, sassy, classy Realtor seeking Web banner for unique innovative Realtor!

Placer County Realtor need web banner re-design. Looking for classy, classic, clean design appealing to elite prospects. Previous focus was short sales now looking to gear towards listing and selling homes, remove short sale focus. Must include, license # 07354218, HE logo, phone, email, etc. check out MaraVoss.com for reference info. I am open to suggestions for other needed content for THE BEST WEB BANNER ON EARTH! LOL. I really want to appeal to the upscale clients, also will be getting away from orange colors going more to a green. Please contact me at MaraVossSells@postvale.net for more info
measurements of banner; Images of exactly 960 × 120 pixels will be used as-is. It's Wordpress Genesis.

I'm really looking for something clean that looks upscale and luxury, classy. 

Please update email address to mara@maravoss.com

Reason: I still haven't gotten what I want. I noticed some really good designs closer to the end here, I'm hoping to allow those folks and maybe a few new ones the opportunity to give me exactly what I want! Thanks!

Reason: I still don't have what I want. I want a simple design that shows that I am a Realtor, maybe a picture of a house???? or something related to real estate. Less emphasis on the Harrowgate Estates logo. Classy and upscale. Fonts should be easy to read but not so simply boring. Please, please, please read the brief!! I REALLY want a good banner!!

Please take a look at the site color adjustment. That's what color it will stay. www.MaraVoss.com

Reason: I'm ready to move this to the end now. I need a design. I'm extending hopefully only this last time to take a vote on them. I will be reaching out to a few select designers to make a few modifications. I appreciate everyone's time on this as you know this is a very tough and important decision to make.

Reason: Need more input

Reason: still trying to decide

upscale home sellers

Realtor

• License # 07354218
Phone (916)555-0147
HE LOGO (attached)
areas of service- Roseville, Rocklin, Granite Bay
MaraVossSells@postvale.net

```html
<!DOCTYPE html>
<html lang="en">
<head>
<meta charset="utf-8">
<title>Mara Voss – Realtor Banner</title>
<link rel="stylesheet" href="https://fonts.googleapis.com/css2?family=Ultra&family=Crimson+Text:wght@400;600&display=swap">
<style>
  :root {
    --green-top: #3f9a3f;
    --green-mid: #6cc265;
    --green-low: #4aa848;
    --navy: #14213d;
    --band: #141c38;
    --white: #ffffff;
    --portrait-a: #c9a27c;
    --portrait-b: #5a8f4e;
  }
  html, body {
    margin: 0;
    padding: 0;
    overflow: hidden;
    background: #ffffff;
  }
  .banner {
    position: relative;
    width: 1200px;
    height: 150px;
    overflow: hidden;
    background: linear-gradient(180deg, var(--green-top) 0%, var(--green-mid) 35%, var(--green-mid) 60%, var(--green-low) 100%);
  }
  .portrait {
    position: absolute;
    left: 0;
    top: 0;
    width: 136px;
    height: 150px;
    background: linear-gradient(135deg, var(--portrait-a) 0%, #d8b48c 45%, var(--portrait-b) 100%);
  }
  .agent-name {
    position: absolute;
    left: 300px;
    width: 520px;
    top: 6px;
    margin: 0;
    text-align: center;
    font-family: "Ultra", serif;
    font-weight: 400;
    font-size: 62px;
    line-height: 80px;
    color: var(--navy);
    letter-spacing: 1px;
  }
  .tagline {
    position: absolute;
    left: 420px;
    top: 88px;
    margin: 0;
    font-family: "Crimson Text", serif;
    font-size: 14px;
    line-height: 18px;
    color: var(--white);
    letter-spacing: 0.3px;
  }
  .brokerage {
    position: absolute;
    left: 972px;
    top: 22px;
    width: 196px;
    height: 88px;
    display: flex;
    align-items: center;
    justify-content: center;
    gap: 10px;
  }
  .brokerage-square {
    width: 14px;
    height: 14px;
    background: var(--navy);
    flex: none;
  }
  .brokerage-name {
    font-family: "Crimson Text", serif;
    font-weight: 600;
    font-size: 22px;
    line-height: 24px;
    color: var(--navy);
  }
  .contact-band {
    position: absolute;
    left: 132px;
    top: 121px;
    width: 1068px;
    height: 25px;
    background: var(--band);
    display: flex;
    align-items: center;
    padding-left: 14px;
    box-sizing: border-box;
    font-family: "Crimson Text", serif;
    font-size: 16px;
    color: var(--white);
    white-space: nowrap;
  }
  .contact-band .sep { padding: 0 6px; }
</style>
</head>
<body>
  <div class="banner">
    <div class="portrait" role="img" aria-label="Portrait photo of the realtor"></div>
    <h1 class="agent-name">Mara Voss</h1>
    <p class="tagline">EXPERIENCED IN LISTING AND SELLING HOMES</p>
    <div class="brokerage">
      <span class="brokerage-square"></span>
      <span class="brokerage-name">Harrowgate Estates</span>
    </div>
    <div class="contact-band">
      <span>License #07354218</span><span class="sep">|</span>
      <span>Phone: 916 555 0147</span><span class="sep">|</span>
      <span>Email: MaraVossSells@postvale.net</span><span class="sep">|</span>
      <span>Area of service Roseville, Rocklin, Granite Bay</span>
    </div>
  </div>
</body>
</html>
```